Owen Tasker Studios Business Card

Looking for a clear, modern, elegant, sharp business card that conveys a professional yet edgy image to my business as a wedding, portrait, and travel photographer. Would like something that looks vintage yet modern. Need a new business card to grow my business. We are growing the business for Wedding and Event Photography as well as fine art Photography. (Mostly Landscapes)
Updates

I’m looking through designs now but I have a new logo that i want using please.

New logo uploaded please redesign using that

PLEASE ALL DESIGNERS LOOK IN BRIEF FOR NEW LOGO

Target Market(s)

Brides, Grooms, Families with Kids, People looking for Fine Art Photography Artwork

Industry/Entity Type

Photographer

Contact Information for Business Card

Unsure

Font styles to use
Serif

Colors

Designer to choose colors to be used in the design.

Requirements
Must have
• My Website:
• http://taskerlens.examplefolio.net
• Phone:
• 323-481-5206
• Email:
• owentaskerlens@mailbox-example.net
Nice to have
• Would like a sort of shine on the printing finish.
• I like black I think it looks good on a business card.
• Can try working with my logo (png that I've attached)

```html
<!DOCTYPE html>
<html lang="en">
<head>
<meta charset="utf-8">
<title>Owen Tasker Studios Business Card</title>
<link href="https://fonts.googleapis.com/css2?family=Jost:wght@300;400&display=swap" rel="stylesheet">
<style>
  :root {
    --backdrop: #2e2e2e;
    --paper: #ffffff;
    --ink: #111111;
    --card-black: #0b0b0b;
    --gloss: #1f1f1f;
    --gloss-edge: #2a2a2a;
  }
  * { box-sizing: border-box; margin: 0; padding: 0; }
  html, body {
    width: 1200px; height: 900px; overflow: hidden;
    background: var(--backdrop);
    font-family: "Jost", "Helvetica Neue", Arial, sans-serif;
  }
  .canvas {
    width: 1200px; height: 900px;
    display: flex; align-items: center; justify-content: center; gap: 40px;
  }
  .card {
    position: relative;
    width: 540px; height: 309px;
    border-radius: 22px;
    box-shadow: 0 10px 30px rgba(0,0,0,.45);
  }

  /* Front */
  .card--front { background: var(--paper); color: var(--ink); }
  .front__name {
    position: absolute; left: 40px; top: 34px;
    font-weight: 300; font-size: 28px; letter-spacing: .5px; line-height: 1;
  }
  .front__title {
    position: absolute; left: 42px; top: 68px;
    font-size: 11px; font-weight: 400; letter-spacing: 5px;
  }
  .rule { position: absolute; left: 40px; width: 66px; height: 3px; background: var(--ink); }
  .rule--top { top: 98px; }
  .rule--bottom { top: 190px; }
  .contact {
    position: absolute; left: 40px;
    display: flex; align-items: center; gap: 10px;
    font-size: 13px; font-weight: 400;
  }
  .contact svg { width: 14px; height: 14px; flex: none; }
  .contact--phone { top: 122px; }
  .contact--email { top: 150px; }
  .contact--web { top: 256px; }

  .front__brand {
    position: absolute; right: 40px; top: 112px;
    width: 150px;
    display: flex; flex-direction: column; align-items: center; gap: 12px;
  }
  .brand-square { width: 70px; height: 70px; border: 2px solid var(--ink); }
  .brand-name {
    font-size: 12px; font-weight: 400; letter-spacing: 2px;
    text-transform: uppercase; text-align: center; line-height: 1.5;
  }

  /* Back */
  .card--back { background: var(--card-black); }
  .back__brand {
    position: absolute; inset: 0;
    display: flex; flex-direction: column; align-items: center; justify-content: center;
    color: var(--gloss);
  }
  .back__square { width: 74px; height: 74px; border: 2px solid var(--gloss-edge); margin-bottom: 10px; }
  .back__name {
    font-size: 40px; font-weight: 300; letter-spacing: .5px; line-height: 1;
    text-transform: uppercase;
  }
  .back__studios {
    margin-top: 8px;
    font-size: 14px; font-weight: 400; letter-spacing: 12px;
    text-transform: uppercase; padding-left: 12px;
  }
</style>
</head>
<body>
<main class="canvas">
  <section class="card card--front">
    <h1 class="front__name">OWEN TASKER</h1>
    <p class="front__title">PHOTOGRAPHER</p>
    <span class="rule rule--top"></span>

    <p class="contact contact--phone">
      <svg viewBox="0 0 16 16" aria-hidden="true"><path fill="#111" d="M1 5c0-2 3-3 7-3s7 1 7 3v1h-4V5H5v1H1zM3 7h10l1 7H2zm5 2a2 2 0 100 4 2 2 0 000-4z"/></svg>
      323-481-5206
    </p>
    <p class="contact contact--email">
      <svg viewBox="0 0 16 16" aria-hidden="true"><path fill="#111" d="M1 3h14v10H1zm1 1.5V12h12V4.5L8 9z"/><path fill="#111" d="M1 3l7 5 7-5z"/></svg>
      owentaskerlens@mailbox-example.net
    </p>
    <span class="rule rule--bottom"></span>
    <p class="contact contact--web">
      <svg viewBox="0 0 16 16" aria-hidden="true"><g fill="none" stroke="#111" stroke-width="1.2"><circle cx="8" cy="8" r="6.5"/><ellipse cx="8" cy="8" rx="3" ry="6.5"/><path d="M1.5 8h13M2.5 5h11M2.5 11h11"/></g></svg>
      taskerlens.examplefolio.net
    </p>

    <div class="front__brand">
      <span class="brand-square"></span>
      <span class="brand-name">Owen Tasker Studios</span>
    </div>
  </section>

  <section class="card card--back">
    <div class="back__brand">
      <span class="back__square"></span>
      <span class="back__name">Owen Tasker</span>
      <span class="back__studios">Studios</span>
    </div>
  </section>
</main>
</body>
</html>
```